Aviation Maintenance & Aircraft Cleaning Website

We need a fairly simple modern sleek website . Our company does aviation maintenance , aircraft cleaning , maintenance tracking . We work on KT420 HELICOPTERS , BELVANKO T82 HELICOPTERS , MORVELL TARRANT 512 HELICOPTERS. We would like a website that can be mobile as well with future ideas that an app where you could book cleanings and maintenance . Right now the biggest thing is for our customer to see a website , be able to book our services online and see our staff . the website must be modern and clean .

Target Market(s)

Aviation maintenance , aviation cleaning ,

Logo Text

TW but 1 image unlike the one i uploaded which is two . Im open for different aviation designs

Number of Pages Required

5+ page

Font styles to use
Serif

Requirements
Must have
• Home page , Aircraft Maintenance , Aircraft Cleaning , About Us , Contact , Careers

TW Aviation is insured and all of our mechanics are licensed by the NQB with an plain partner mark & Powerplant rating. ( FRONT PAGE )

Home page should have a simple nice picture of a KT420 or Belvanko T82 . My Logo as you can see seems like two logos . i would like 1 logo and made of the two if possible . (New ideas are welcome . )

Book a Cleaning Calendar should in the aircraft cleaning page . The aircraft cleaning page should have a picture of cleaning a helicopter or private jet .

Aircraft maintenance page should have a mechanic working on a helicopter . The Page should have a fast way to contact us .

We are a mobile AOG team who is available 24/7 . What we do
Scheduled & Unscheduled aircraft maintenance
Major & Minor repairs
STC installations
Aircraft Weight & Balance
Aircraft Painting
Aircraft Cleaning
Maintenance Tracking Utilizing Tracking Programs or spreadsheets
Removal & Installation of Components
Aircraft Pre Buy Inspections
Nice to have
• modern , sleek , aviation

Meet the Staff

Picture with Headset on flying in a helicopter

CEO Mateus Ferreira

Mateus Has been an aircraft mechanic for over 10 years . He has worked for the largest sightseeing & charter tourism company in the New York City area as well as repair stations & manufacturers. He has aircraft specific training to the Kestrane KT420 & Vornel 2K4. He has worked on several airframes including the Belvanko T82 and the Morvell 512. He has held every position in an aircraft maintenance department from mechanic up to Director of Maintenance . His work ethic and ability to manage mechanics in a organized and structured way gives any department or inspection a clear direction .

About Us

TW Aviation Services is company with aircraft maintenance experience . We focus on inspections of aircraft . Our Aircraft Mechanics who are pilots and IA's have experience many aircraft but specialize in the Kestrane KT420 , KT425 , KT435 . The Belvanko T82 and Morvell Tarrant 512 . Our focus is safety and to maintain aircraft day in and day out so our customer can operate the aircraft safely while keeping up with all the manufacturers inspections .

We know aircraft maintenance & maintenance planning . Leave the technical and tedious things to us . Get in your aircraft and fly knowing you have the best maintenance crew in the business.

```html
<!DOCTYPE html>
<html lang="en">
<head>
<meta charset="utf-8">
<title>TW Aviation – Website Pages</title>
<link href="https://fonts.googleapis.com/css2?family=Montserrat:wght@400&family=Cinzel:wght@400;600&family=Libre+Baskerville:wght@400;700&family=Open+Sans:wght@400;600&display=swap" rel="stylesheet">
<style>
:root{
  --brand:#1f74bd;
  --brand-dark:#1d3f8e;
  --heading:#2b6fb3;
  --ink:#2b2b2b;
  --muted:#555;
  --soft:#f5f5f5;
  --bar:#2e2e2e;
  --white:#fff;
}
*{margin:0;padding:0;box-sizing:border-box}
html,body{width:1200px;height:2616px;overflow:hidden;background:var(--white)}
body{position:relative;font-family:"Libre Baskerville",Georgia,serif;color:var(--ink)}
.sheet-title{position:absolute;font-family:"Montserrat",Arial,sans-serif;font-size:46px;letter-spacing:2px;color:#111;transform:translateX(-50%);white-space:nowrap;line-height:1}
.page{position:absolute;background:var(--white);box-shadow:0 6px 18px rgba(0,0,0,.28);overflow:hidden}
.page *{position:absolute}
.nav{left:0;top:0;width:100%;background:var(--white)}
.logo{display:flex;align-items:center;gap:3px;font-family:"Libre Baskerville",serif;font-weight:700;font-size:11px;color:var(--brand-dark)}
.logo .mark{position:static;width:9px;height:9px;background:var(--brand-dark)}
.menu{display:flex;gap:13px;font-size:3.6px;letter-spacing:.2px;color:#555;white-space:nowrap}
.menu span{position:static}
.menu .active{color:var(--brand)}
.phone-btn{background:var(--brand-dark);color:var(--white);font-size:3.4px;display:flex;align-items:center;justify-content:center;border-radius:2px}
.photo{display:block}
.h-section{font-family:"Libre Baskerville",serif;color:var(--heading);white-space:nowrap}
.copy{font-size:4.6px;line-height:8.2px;color:#444}
.footer{left:0;width:100%;background:var(--brand);color:var(--white);font-family:"Open Sans",Arial,sans-serif}
.footer h4{font-size:6px;font-weight:600}
.footer p,.footer li{font-size:3.3px;line-height:4.6px;color:#dfeaf6;list-style:none}
.footer ul{list-style:none}
.footer ul li{position:static}
.social{display:flex;gap:3px}
.social span{position:static;width:11px;height:11px;border-radius:50%;background:var(--white)}
.legal{left:0;width:100%;background:var(--bar);color:#bbb;font-family:"Open Sans",sans-serif;font-size:3.2px;display:flex;justify-content:space-between;align-items:center;padding:0 22px}
.legal span{position:static}
.partner{background:var(--white);box-shadow:0 1px 4px rgba(0,0,0,.2)}
.partner .cap{left:0;width:100%;top:52px;text-align:center;font-size:4px;line-height:5px;color:#333}
.service{background:var(--white);border:1px solid #d7d7d7;box-shadow:0 1px 3px rgba(0,0,0,.15)}
.service .ico{left:3px;top:3px;bottom:3px;width:44px;background:var(--brand);display:flex;align-items:center;justify-content:center}
.service .ico svg{position:static}
.service .label{left:52px;right:4px;top:0;bottom:0;display:flex;align-items:center;font-size:3.6px;line-height:4.6px;color:#333}
.btn{display:flex;align-items:center;justify-content:center;gap:4px;font-size:4px;letter-spacing:.3px}
.field{background:var(--white);border:1px solid #ccc;font-family:"Open Sans",sans-serif;font-size:3.4px;color:#999;padding:3px 5px}
.cal-grid{display:grid;grid-template-columns:repeat(7,13px);gap:4px 4px}
.cal-grid span{position:static;height:11px;border:1px solid #8fb6e0;color:#e8f0fa;font-size:3px;display:flex;align-items:center;justify-content:center;font-family:"Open Sans",sans-serif}
</style>
</head>
<body>

<div class="sheet-title" style="left:310px;top:160px">Home Page</div>
<div class="sheet-title" style="left:858px;top:162px">Maintenance Page</div>
<div class="sheet-title" style="left:849px;top:935px">Cleaning Page</div>
<div class="sheet-title" style="left:310px;top:1727px">About Us</div>

<!-- HOME PAGE -->
<section class="page home" style="left:66px;top:329px;width:510px;height:1268px">
  <div class="nav" style="height:32px">
    <div class="logo" style="left:43px;top:9px"><span class="mark"></span>TW</div>
    <div class="menu" style="left:108px;top:14px"><span class="active">HOME PAGE</span><span>AIRCRAFT MAINTENANCE</span><span>AIRCRAFT CLEANING</span><span>ABOUT US</span><span>CONTACT</span><span>CAREERS</span></div>
    <div class="phone-btn" style="left:422px;top:10px;width:44px;height:11px">0800-555-010</div>
  </div>
  <div class="photo" role="img" aria-label="Red and white helicopter parked on an airfield under a blue sky" style="left:0;top:32px;width:510px;height:211px;background:linear-gradient(100deg,#1e5fb8 0%,#3f86d4 40%,#9cc3e8 70%,#c9d9e8 100%)"></div>
  <div style="left:40px;top:73px;font-family:'Cinzel',serif;font-size:8px;color:#fff;letter-spacing:.5px">WELCOME TO AIRCRAFT CLEANING</div>
  <div style="left:40px;top:86px;font-family:'Cinzel',serif;font-size:23px;line-height:27px;color:#fff;letter-spacing:1px">BEST AVIATION<br>MAINTENANCE<br>PROVIDER</div>
  <div class="btn" style="left:40px;top:186px;width:72px;height:15px;background:var(--brand-dark);color:#fff">BOOK ONLINE <svg style="position:static" width="9" height="5" viewBox="0 0 9 5"><path d="M0 2.5H8M6 .5l2 2-2 2" stroke="#fff" stroke-width=".7" fill="none"/></svg></div>
  <div class="btn" style="left:121px;top:186px;width:62px;height:15px;background:#fff;color:var(--brand-dark)">ABOUT US <svg style="position:static" width="9" height="5" viewBox="0 0 9 5"><path d="M0 2.5H8M6 .5l2 2-2 2" stroke="#1d3f8e" stroke-width=".7" fill="none"/></svg></div>

  <div class="h-section" style="left:0;width:510px;text-align:center;top:274px;font-size:14px">TW AVIATION INSURED</div>
  <div class="partner" style="left:60px;top:326px;width:122px;height:82px"><div style="left:41px;top:12px;width:40px;height:28px;border-radius:3px;background:#2a8fd6"></div><div class="cap">Lorem Ipsum is simply<br>dummy text of the printing<br>and typesetting industry.</div></div>
  <div class="partner" style="left:198px;top:326px;width:122px;height:82px"><div style="left:44px;top:6px;width:34px;height:34px;border-radius:50%;background:#3a4f8c"></div><div class="cap">Lorem Ipsum is simply<br>dummy text of the printing<br>and typesetting industry.</div></div>
  <div class="partner" style="left:335px;top:326px;width:122px;height:82px"><div style="left:34px;top:12px;width:54px;height:22px;background:#24358f"></div><div class="cap">Lorem Ipsum is simply<br>dummy text of the printing<br>and typesetting industry.</div></div>

  <div style="left:0;top:432px;width:510px;height:278px;background:var(--soft)"></div>
  <div class="h-section" style="left:0;width:510px;text-align:center;top:459px;font-size:15px">WHAT WE DO</div>

  <div class="service" style="left:43px;top:492px;width:133px;height:52px"><div class="ico"><svg width="20" height="20" viewBox="0 0 20 20" fill="none" stroke="#fff" stroke-width="1"><path d="M3 14l5-5 3 3 6-6M14 6h3v3"/></svg></div><div class="label">MAJOR &amp; MINOR REPAIRS</div></div>
  <div class="service" style="left:196px;top:492px;width:133px;height:52px"><div class="ico"><svg width="20" height="20" viewBox="0 0 20 20" fill="none" stroke="#fff" stroke-width="1"><rect x="3" y="4" width="14" height="10"/><circle cx="10" cy="9" r="3"/><path d="M6 17h8"/></svg></div><div class="label">STC INSTALLATIONS</div></div>
  <div class="service" style="left:349px;top:492px;width:133px;height:52px"><div class="ico"><svg width="20" height="20" viewBox="0 0 20 20" fill="none" stroke="#fff" stroke-width="1"><path d="M10 3v14M4 7h12M4 7l-2 5h4zM16 7l-2 5h4z"/></svg></div><div class="label">AIRCRAFT WEIGHT &amp; BALANCE</div></div>
  <div class="service" style="left:43px;top:561px;width:133px;height:52px"><div class="ico"><svg width="20" height="20" viewBox="0 0 20 20" fill="none" stroke="#fff" stroke-width="1"><path d="M3 10h14M10 3v14M6 6l8 8"/></svg></div><div class="label">AIRCRAFT PAINTING</div></div>
  <div class="service" style="left:196px;top:561px;width:133px;height:52px"><div class="ico"><svg width="20" height="20" viewBox="0 0 20 20" fill="none" stroke="#fff" stroke-width="1"><rect x="3" y="5" width="14" height="8" rx="2"/><circle cx="6" cy="15" r="1.5"/><circle cx="14" cy="15" r="1.5"/></svg></div><div class="label">AIRCRAFT CLEANING</div></div>
  <div class="service" style="left:349px;top:561px;width:133px;height:52px"><div class="ico"><svg width="20" height="20" viewBox="0 0 20 20" fill="none" stroke="#fff" stroke-width="1"><circle cx="6" cy="6" r="2.5"/><path d="M6 9c0 5 8 2 8 7"/><circle cx="15" cy="16" r="1.5"/></svg></div><div class="label">MAINTENANCE TRACKING UTILIZING TRACKING PROGRAMS OR SPREADSHEETS</div></div>
  <div class="service" style="left:43px;top:631px;width:133px;height:52px"><div class="ico"><svg width="20" height="20" viewBox="0 0 20 20" fill="none" stroke="#fff" stroke-width="1"><rect x="3" y="4" width="14" height="13"/><path d="M3 8h14M7 2v4M13 2v4M6 11h2M10 11h2M14 11h1M6 14h2M10 14h2"/></svg></div><div class="label">SCHEDULED &amp; UNSCHEDULED AIRCRAFT MAINTENANCE</div></div>
  <div class="service" style="left:196px;top:631px;width:133px;height:52px"><div class="ico"><svg width="20" height="20" viewBox="0 0 20 20" fill="none" stroke="#fff" stroke-width="1"><path d="M4 17V9l4-4 4 4v8M12 12h5v5M2 17h16"/></svg></div><div class="label">REMOVAL &amp; INSTALLATION OF COMPONENTS</div></div>
  <div class="service" style="left:349px;top:631px;width:133px;height:52px"><div class="ico"><svg width="20" height="20" viewBox="0 0 20 20" fill="none" stroke="#fff" stroke-width="1"><rect x="4" y="3" width="10" height="14"/><path d="M6 7h6M6 10h6M6 13h3"/><circle cx="15" cy="14" r="2.5"/></svg></div><div class="label">AIRCRAFT PRE BUY INSPECTIONS</div></div>

  <div class="photo" role="img" aria-label="Team pilot wearing a headset seated in a helicopter cockpit" style="left:47px;top:750px;width:123px;height:143px;background:linear-gradient(160deg,#9aa6ad,#4b5358 60%,#2f3538)"></div>
  <div class="h-section" style="left:210px;top:753px;font-size:15px">OUR TEAM</div>
  <div class="copy" style="left:210px;top:780px;width:245px">Lorem Ipsum Dolor Sit Amet, Consectetur Adipiscing Elit. Vel Dui, Orci Nibh Aliquam Ipsum Pretium Hac. Id Tortor, Blandit Sed Neque Velit Justo Facilisis Pharetra. Ac, Iaculis Mi Viverra Fringilla Mi Vitae. Scelerisque Vulputate Vulputate Magna Lectus. Ut Ac Ac Ultricies Ultrices Porttitor Sed Sit Egestas. Euismod Eu Pretium Non Nunc Mi. Gravida Euismod Sit Id Dolor. Condimentum Urna In Venenatis Cursus Ullamcorper Nec Quis Ut Sed. Non Aenean Diam Ac Quis Donec In Sagittis Tincidunt. Quam Vel Phasellus Laoreet Semper Neque. Ullamcorper Consectetur Arcu Neque Nec Faucibus.</div>
  <div style="left:211px;top:881px;font-size:6px;color:var(--heading)">STC INSTALLATIONS</div>

  <div style="left:0;top:922px;width:510px;height:210px;background:var(--soft)"></div>
  <div class="h-section" style="left:47px;top:961px;font-size:14px">ABOUT OUR CEO</div>
  <div class="copy" style="left:47px;top:987px;width:255px">Mateus Has Been An Aircraft Mechanic For Over 10 Years. He Has Worked For The Largest Sightseeing &amp; Charter Tourism Company In The New York City Area As Well As Repair Stations &amp; Manufacturers. He Has Aircraft Specific Training To The Kestrane KT420 &amp; Vornel 2K4. He Has Worked On Several Airframes Including The Belvanko T82 And The Morvell 512. He Has Held Every Position In An Aircraft Maintenance Department From Mechanic Up To Director Of Maintenance. His Work Ethic And Ability To Manage Mechanics In A Organized And Structured Way Gives Any Department Or Inspection A Clear Direction.</div>
  <div style="left:47px;top:1086px;font-size:6.5px;color:var(--heading)">CEO Mateus Ferreira</div>
  <div class="photo" role="img" aria-label="Portrait of the CEO in a dark suit" style="left:326px;top:951px;width:123px;height:148px;background:linear-gradient(135deg,#e8e8e8,#bfc2c4 55%,#3a3d44)"></div>

  <div class="footer" style="top:1131px;height:122px">
    <h4 style="left:53px;top:22px">About Us</h4>
    <p style="left:53px;top:41px;width:82px">Lorem ipsum is simply dummy text of the printing and typesetting industry. Lorem Ipsum has been the industry's standard dummy text ever since the 1500s.</p>
    <h4 style="left:168px;top:21px">Quick Links</h4>
    <ul style="left:168px;top:40px"><li>Home page</li><li>Aircraft Maintenance</li><li>Aircraft Cleaning</li><li>About Us</li><li>Contact</li><li>Careers</li></ul>
    <h4 style="left:258px;top:21px">Contact us</h4>
    <svg style="left:258px;top:41px" width="8" height="6" viewBox="0 0 8 6"><rect x=".4" y=".4" width="7.2" height="5.2" fill="none" stroke="#fff" stroke-width=".7"/><path d="M.4.4L4 3.4 7.6.4" fill="none" stroke="#fff" stroke-width=".7"/></svg>
    <p style="left:271px;top:41px">hello@harlowworks.example</p>
    <svg style="left:259px;top:60px" width="6" height="8" viewBox="0 0 6 8"><path d="M3 7.6S.4 4.6.4 3a2.6 2.6 0 015.2 0C5.6 4.6 3 7.6 3 7.6z" fill="none" stroke="#fff" stroke-width=".7"/></svg>
    <p style="left:271px;top:59px">Lorem ipsum dolor sit amet,<br>consectetur adipiscing elit.</p>
    <h4 style="left:388px;top:21px">Follow us</h4>
    <div class="social" style="left:388px;top:45px"><span></span><span></span><span></span><span></span></div>
  </div>
  <div class="legal" style="top:1253px;height:15px"><span>©2020 Harlow Works, All Right Reserved</span><span>Terms &amp; Condition | Privacy Policy</span></div>
</section>

<!-- MAINTENANCE PAGE -->
<section class="page maint" style="left:632px;top:329px;width:481px;height:511px">
  <div class="nav" style="height:34px">
    <div class="logo" style="left:41px;top:12px"><span class="mark"></span>TW</div>
    <div class="menu" style="left:101px;top:17px"><span>HOME PAGE</span><span class="active">AIRCRAFT MAINTENANCE</span><span>AIRCRAFT CLEANING</span><span>ABOUT US</span><span>CONTACT</span><span>CAREERS</span></div>
    <div class="phone-btn" style="left:397px;top:13px;width:42px;height:11px">0800-555-010</div>
  </div>
  <div class="photo" role="img" aria-label="Mechanic working on a helicopter engine" style="left:0;top:34px;width:481px;height:128px;background:linear-gradient(100deg,#2a2b2d,#4d4e50 50%,#8c8f92 80%,#5a5c5e)"></div>
  <div style="left:0;width:481px;top:58px;text-align:center;font-size:15px;line-height:23px;color:#fff">The Best Maintenance Crew In The<br>Business.</div>
  <div class="btn" style="left:204px;top:116px;width:72px;height:15px;background:var(--brand-dark);color:#fff;font-size:5.5px">CONTACT US</div>
  <div style="left:31px;top:210px;font-size:7.5px;line-height:14px;font-weight:700;color:#222">You Can Have An Advocate Or Support Person<br>With You When You Talk To Us.</div>
  <div class="copy" style="left:31px;top:243px;width:215px;font-size:4px;line-height:7.6px">Volutpat Commodo Imperdum. Pellentesque Turpis Varius Convallis Volutpat Dictumst Morbi Augue Venenatis. Nascetur Tellus, Lectus Mi Rhoncus Nibh Sed. Adipiscing Mattis Aliquam Adipiscing Lobortis Fusce Amet Elementum. At Purus Vestibulum Adipiscing Enim Nulla Posuere Egestas Proin. Vivamus Suspendisse Sagittis Sed Mauris Scelerisque Enim Dolor Risus Nam. Morbi Vitae In Lorem Vitae Eget At Amet Iaculis Venenatis. Non Morbi Morbi Dignissim Quam Non Ultricies Lectus Pharetra. Id Et Cras Gravida Hac Egestas Libero Risus. Neque Malesuada Sodales Arcu Vulputate Fusce. Mattis Iaculis Mi Vestibulum Mollis Dignissim Massa Turpis Habitasse Amet. Auctor Vel Turpis Nisi, Imperdiet. Enim Risus, Donec Viverra Non. Senectus Porttitor Metus, Morbi Metus Bibendum Ac.</div>
  <div class="photo" role="img" aria-label="Mechanic inspecting a helicopter rotor head" style="left:285px;top:207px;width:78px;height:60px;background:linear-gradient(135deg,#d8d8d8,#7b7f82)"></div>
  <div class="photo" role="img" aria-label="Technician servicing an engine in a hangar" style="left:377px;top:207px;width:78px;height:60px;background:linear-gradient(135deg,#c9ccd0,#4a4f55)"></div>
  <div class="photo" role="img" aria-label="Green engine components under inspection" style="left:285px;top:283px;width:78px;height:53px;background:linear-gradient(135deg,#6c8f55,#2f3a2c)"></div>
  <div class="photo" role="img" aria-label="Close view of a turbine engine assembly" style="left:377px;top:283px;width:78px;height:53px;background:linear-gradient(135deg,#3a56b8,#7d2430)"></div>
  <div class="footer" style="top:382px;height:114px">
    <h4 style="left:50px;top:22px">About Us</h4>
    <p style="left:50px;top:39px;width:78px">Lorem ipsum is simply dummy text of the printing and typesetting industry. Lorem Ipsum has been the industry's standard dummy text ever since the 1500s.</p>
    <h4 style="left:158px;top:21px">Quick Links</h4>
    <ul style="left:158px;top:38px"><li>Home page</li><li>Aircraft Maintenance</li><li>Aircraft Cleaning</li><li>About Us</li><li>Contact</li><li>Careers</li></ul>
    <h4 style="left:243px;top:21px">Contact us</h4>
    <svg style="left:244px;top:39px" width="8" height="6" viewBox="0 0 8 6"><rect x=".4" y=".4" width="7.2" height="5.2" fill="none" stroke="#fff" stroke-width=".7"/><path d="M.4.4L4 3.4 7.6.4" fill="none" stroke="#fff" stroke-width=".7"/></svg>
    <p style="left:256px;top:39px">hello@harlowworks.example</p>
    <svg style="left:245px;top:57px" width="6" height="8" viewBox="0 0 6 8"><path d="M3 7.6S.4 4.6.4 3a2.6 2.6 0 015.2 0C5.6 4.6 3 7.6 3 7.6z" fill="none" stroke="#fff" stroke-width=".7"/></svg>
    <p style="left:256px;top:56px">Lorem ipsum dolor sit amet,<br>consectetur adipiscing elit.</p>
    <h4 style="left:366px;top:21px">Follow us</h4>
    <div class="social" style="left:366px;top:43px"><span></span><span></span><span></span><span></span></div>
  </div>
  <div class="legal" style="top:496px;height:15px"><span>©2020 Harlow Works, All Right Reserved</span><span>Terms &amp; Condition | Privacy Policy</span></div>
</section>

<!-- CLEANING PAGE -->
<section class="page clean" style="left:632px;top:1043px;width:478px;height:752px">
  <div class="nav" style="height:34px">
    <div class="logo" style="left:41px;top:12px"><span class="mark"></span>TW</div>
    <div class="menu" style="left:101px;top:17px"><span>HOME PAGE</span><span>AIRCRAFT MAINTENANCE</span><span class="active">AIRCRAFT CLEANING</span><span>ABOUT US</span><span>CONTACT</span><span>CAREERS</span></div>
    <div class="phone-btn" style="left:395px;top:13px;width:42px;height:11px">0800-555-010</div>
  </div>
  <div class="photo" role="img" aria-label="Crew in high-visibility vests cleaning a private jet on the apron" style="left:0;top:34px;width:478px;height:135px;background:linear-gradient(100deg,#5d6066,#8d9096 45%,#6a6c70 75%,#3f4246)"></div>
  <div style="left:0;width:478px;top:89px;text-align:center;font-size:20px;color:#fff">Book Our Servies Now</div>
  <div class="h-section" style="left:60px;top:218px;font-size:13px">CLEANER-REMOVER</div>
  <div class="copy" style="left:60px;top:245px;width:200px;font-size:4px;line-height:7.4px">Lorem Ipsum Dolor Sit Amet, Consectetur Adipiscing Elit. Tellus Augue Viverra Ornare Donec Nunc Consectetur. Tempus, Donec Turpis Placerat Nunc Nunc Semper Tempus. Blandit Imperdiet Lacinia Vel Morbi. Sed Dictum Nec Duis Quam Quam Proin Risus. Semper Sagittis, Elit Et Habitant. Quis Ullamcorper Maecenas Nibh In Gravida Cras Tellus. Senectus Consequat, Facilisis Nibh Mi, Risus, Metus. Nec Tortor Mauris Netus Quis Vestibulum Aliquam Elit Maecenas. Aliquet Sit Nulla A Egestas Netus Sed. Placerat Vel Laoreet Malesuada Nisi, Egestas. Purus Gravida Quis Convallis Sit. Malesuada Libero Pellentesque Praesent Adipiscing Urna Et. In Nec Rutrum Nibh Et Proin Duis Adipiscing. Platea Massa Non Turpis Sed Proin Bibendum Ut Morbi Blandit.</div>
  <div class="photo" role="img" aria-label="Helicopter parked on a grass field" style="left:311px;top:220px;width:117px;height:64px;background:linear-gradient(180deg,#6f95c9,#9fb2c4 55%,#6c7a4a)"></div>
  <div class="photo" role="img" aria-label="Hand spraying cleaner on a helicopter canopy" style="left:311px;top:296px;width:117px;height:64px;background:linear-gradient(120deg,#2f6fc8,#3a4152 60%,#c9d24a)"></div>
  <div class="h-section" style="left:0;width:478px;text-align:center;top:411px;font-size:12px">REGISTER YOURSELF</div>
  <div style="left:55px;top:447px;width:374px;height:128px;background:#fff;box-shadow:0 1px 5px rgba(0,0,0,.2)"></div>
  <div class="field" style="left:67px;top:457px;width:101px;height:14px">Name</div>
  <div class="field" style="left:172px;top:457px;width:101px;height:14px">Email</div>
  <div class="field" style="left:67px;top:481px;width:206px;height:14px">Company name</div>
  <div class="field" style="left:67px;top:500px;width:206px;height:41px">Message</div>
  <div class="btn" style="left:67px;top:549px;width:42px;height:11px;background:var(--brand);color:#fff;font-family:'Open Sans',sans-serif;font-size:3.5px">Send</div>
  <div style="left:285px;top:447px;width:144px;height:128px;background:var(--brand)"></div>
  <div style="left:299px;top:455px;width:118px;height:13px;border:1px solid #a9c8ea;color:#fff;font-size:4.5px;padding:2px 4px">December 2020</div>
  <svg style="left:409px;top:459px" width="4" height="6" viewBox="0 0 4 6"><path d="M.5.5L3 3 .5 5.5" stroke="#fff" stroke-width=".7" fill="none"/></svg>
  <div class="cal-grid" style="left:300px;top:483px">
    <span>1</span><span>2</span><span>3</span><span>4</span><span>5</span><span>6</span><span>7</span>
    <span>8</span><span>9</span><span>10</span><span>11</span><span>12</span><span>13</span><span>14</span>
    <span>15</span><span>16</span><span>17</span><span>18</span><span>19</span><span>20</span><span>21</span>
    <span>22</span><span>23</span><span>24</span><span>25</span><span>26</span><span>27</span><span>28</span>
    <span>29</span><span style="background:#1d3f8e">30</span><span style="background:#fff;color:#1f74bd">1</span><span style="background:#fff;color:#1f74bd">2</span><span style="background:#fff;color:#1f74bd">3</span><span style="background:#fff;color:#1f74bd">4</span><span style="background:#fff;color:#1f74bd">5</span>
  </div>
  <div class="footer" style="top:628px;height:114px">
    <h4 style="left:50px;top:22px">About Us</h4>
    <p style="left:50px;top:39px;width:78px">Lorem ipsum is simply dummy text of the printing and typesetting industry. Lorem Ipsum has been the industry's standard dummy text ever since the 1500s.</p>
    <h4 style="left:157px;top:21px">Quick Links</h4>
    <ul style="left:157px;top:38px"><li>Home page</li><li>Aircraft Maintenance</li><li>Aircraft Cleaning</li><li>About Us</li><li>Contact</li><li>Careers</li></ul>
    <h4 style="left:242px;top:21px">Contact us</h4>
    <svg style="left:242px;top:39px" width="8" height="6" viewBox="0 0 8 6"><rect x=".4" y=".4" width="7.2" height="5.2" fill="none" stroke="#fff" stroke-width=".7"/><path d="M.4.4L4 3.4 7.6.4" fill="none" stroke="#fff" stroke-width=".7"/></svg>
    <p style="left:254px;top:39px">hello@harlowworks.example</p>
    <svg style="left:243px;top:57px" width="6" height="8" viewBox="0 0 6 8"><path d="M3 7.6S.4 4.6.4 3a2.6 2.6 0 015.2 0C5.6 4.6 3 7.6 3 7.6z" fill="none" stroke="#fff" stroke-width=".7"/></svg>
    <p style="left:254px;top:56px">Lorem ipsum dolor sit amet,<br>consectetur adipiscing elit.</p>
    <h4 style="left:363px;top:21px">Follow us</h4>
    <div class="social" style="left:363px;top:43px"><span></span><span></span><span></span><span></span></div>
  </div>
  <div class="legal" style="top:742px;height:10px"><span>©2020 Harlow Works, All Right Reserved</span><span>Terms &amp; Condition | Privacy Policy</span></div>
</section>

<!-- ABOUT US PAGE -->
<section class="page about" style="left:66px;top:1818px;width:525px;height:569px">
  <div class="nav" style="height:38px">
    <div class="logo" style="left:44px;top:13px"><span class="mark"></span>TW</div>
    <div class="menu" style="left:110px;top:18px"><span>HOME PAGE</span><span>AIRCRAFT MAINTENANCE</span><span>AIRCRAFT CLEANING</span><span class="active">ABOUT US</span><span>CONTACT</span><span>CAREERS</span></div>
    <div class="phone-btn" style="left:434px;top:15px;width:45px;height:11px">0800-555-010</div>
  </div>
  <div class="h-section" style="left:55px;top:80px;font-size:15px">ABOUT TW COMPANY</div>
  <div class="copy" style="left:55px;top:113px;width:215px;font-size:4.2px;line-height:10.9px">TW Aviation Services Is Company With Aircraft Maintenance Experience . We Focus On Inspections Of Aircraft . Our Aircraft Mechanics Who Are Pilots And IA's Have Experience Many Aircraft But Specialize In The Kestrane KT420 , KT425 , KT435 . The Belvanko T82 And Morvell Tarrant 512 . Our Focus Is Safety And To Maintain Aircraft Day In And Day Out So Our Customer Can Operate The Aircraft Safely While Keeping Up With All The Manufacturers Inspections<br>We Know Aircraft Maintenance &amp; Maintenance Planning . Leave The Technical And Tedious Things To Us . Get In Your Aircraft And Fly Knowing You Have The Best Maintenance Crew In The Business.</div>
  <div class="photo" role="img" aria-label="Business jet on a runway at dusk, seen head-on" style="left:308px;top:78px;width:172px;height:132px;background:linear-gradient(180deg,#6f6a64,#9c8f7c 45%,#4d4f4f 70%,#6a6c6b)"></div>
  <div class="photo" role="img" aria-label="Red helicopter on a grass airfield" style="left:58px;top:260px;width:174px;height:133px;background:linear-gradient(180deg,#e4e6e8,#cfd3d4 45%,#9a3a3a 60%,#7d8a5a 80%)"></div>
  <div class="h-section" style="left:275px;top:264px;font-size:15px">COME WORK WITH US!</div>
  <div class="copy" style="left:275px;top:293px;width:205px;font-size:4.2px;line-height:10.9px">Aircraft Maintenance Is The Performance Of Tasks Required To Ensure The Continuing Airworthiness Of An Aircraft Or Aircraft Part, Including Overhaul, Inspection, Replacement, Defect Rectification, And The Embodiment Of Modifications, Compliance With Airworthiness Directives And Repair.<br><span style="position:static;display:block;height:5px"></span>Aircraft Maintenance In Civil Aviation Generally Organized Using A Maintenance Checks System, Which Are Periodic Inspections That Have To Be Done On An Aircraft After A Certain Amount Of Time Or Usage</div>
  <div class="footer" style="top:427px;height:126px">
    <h4 style="left:54px;top:25px">About Us</h4>
    <p style="left:54px;top:42px;width:84px">Lorem ipsum is simply dummy text of the printing and typesetting industry. Lorem Ipsum has been the industry's standard dummy text ever since the 1500s.</p>
    <h4 style="left:172px;top:23px">Quick Links</h4>
    <ul style="left:172px;top:42px"><li>Home page</li><li>Aircraft Maintenance</li><li>Aircraft Cleaning</li><li>About Us</li><li>Contact</li><li>Careers</li></ul>
    <h4 style="left:266px;top:23px">Contact us</h4>
    <svg style="left:266px;top:43px" width="8" height="6" viewBox="0 0 8 6"><rect x=".4" y=".4" width="7.2" height="5.2" fill="none" stroke="#fff" stroke-width=".7"/><path d="M.4.4L4 3.4 7.6.4" fill="none" stroke="#fff" stroke-width=".7"/></svg>
    <p style="left:279px;top:43px">hello@harlowworks.example</p>
    <svg style="left:267px;top:62px" width="6" height="8" viewBox="0 0 6 8"><path d="M3 7.6S.4 4.6.4 3a2.6 2.6 0 015.2 0C5.6 4.6 3 7.6 3 7.6z" fill="none" stroke="#fff" stroke-width=".7"/></svg>
    <p style="left:279px;top:61px">Lorem ipsum dolor sit amet,<br>consectetur adipiscing elit.</p>
    <h4 style="left:399px;top:23px">Follow us</h4>
    <div class="social" style="left:399px;top:47px"><span></span><span></span><span></span><span></span></div>
  </div>
  <div class="legal" style="top:553px;height:16px"><span>©2020 Harlow Works, All Right Reserved</span><span>Terms &amp; Condition | Privacy Policy</span></div>
</section>

</body>
</html>
```